Box truck wrap design for my business BrickNest Seal and Slab

A simple, modern design for a box truck. Truck dimensions are as follows.

Sides - 181"W x 84"H
Back Rollup Door - 87 3/4"W x 85 1/4"H

Brand guidelines have been attached along with examples of wraps that I like. Just need to apply this to an valtro box truck. Website is bricknest-crew.example which you can use as inspiration. Slogan is 'Sealed Tight, Built on Solid Ground"

Target Market(s)

Insulation, Waterproofing, Foundation Repair

Industry/Entity Type

Construction - Home Services

Font styles to use
Other font styles liked:
• use brand guidelines attached

Colors

Designer to choose colors to be used in the design.

Requirements
Must have
• bricknest-crew.example , 555-214-7739

```html
<!DOCTYPE html>
<html lang="en">
<head>
<meta charset="utf-8">
<title>BrickNest Seal and Slab – Box Truck Wrap</title>
<link rel="stylesheet" href="https://fonts.googleapis.com/css2?family=Poppins:ital,wght@0,600;0,700;1,800&family=Michroma&display=swap">
<style>
  :root {
    --bg: #eef0f2;
    --orange: #e5300a;
    --orange-light: #f2561c;
    --black: #0d0d0d;
    --band: #e4e4e4;
    --grey: #8d8f93;
    --grey-mark: #9b9fa5;
    --white: #ffffff;
    --ink: #161616;
  }
  html, body { margin: 0; padding: 0; overflow: hidden; }
  body { width: 1200px; height: 2369px; background: var(--bg); position: relative; }
  .wrap-panel { position: absolute; display: block; }
  .side-left  { left: 76px;  top: 161px;  width: 734px; height: 341px; }
  .side-right { left: 391px; top: 957px;  width: 734px; height: 341px; }
  .door-orange { left: 95px;  top: 1704px; width: 443px; height: 414px; }
  .door-black  { left: 684px; top: 1704px; width: 443px; height: 414px; }
  .services { font-family: 'Poppins', sans-serif; font-weight: 600; font-size: 14px; fill: var(--white); }
  .brand-name { font-family: 'Poppins', sans-serif; font-weight: 700; fill: var(--ink); }
  .subtitle { font-family: 'Michroma', sans-serif; font-size: 15px; fill: var(--white); }
  .tagline { font-family: 'Poppins', sans-serif; font-style: italic; font-weight: 800; font-size: 14px; fill: var(--orange); }
  .phone { font-family: 'Poppins', sans-serif; font-weight: 700; font-size: 26px; fill: var(--white); }
  .web { font-family: 'Poppins', sans-serif; font-weight: 600; font-size: 11.5px; fill: var(--white); }
</style>
</head>
<body>

<svg width="0" height="0" style="position:absolute">
  <defs>
    <radialGradient id="rays-orange" cx="0.55" cy="0.2" r="0.9">
      <stop offset="0" stop-color="#f4601f"/>
      <stop offset="1" stop-color="#e2290a"/>
    </radialGradient>
    <radialGradient id="rays-black" cx="0.5" cy="0.1" r="0.9">
      <stop offset="0" stop-color="#2a2a2a"/>
      <stop offset="1" stop-color="#050505"/>
    </radialGradient>
    <symbol id="phone-icon" viewBox="0 0 24 24">
      <circle cx="12" cy="12" r="10.5" fill="none" stroke="#fff" stroke-width="2"/>
      <path d="M8.6 6.8l1.6 2.4-1 1.3c.7 1.5 1.9 2.7 3.4 3.4l1.3-1 2.4 1.6-.9 2c-4 0-8.8-4.8-8.8-8.8z" fill="#fff"/>
    </symbol>
  </defs>
</svg>

<!-- Driver side -->
<svg class="wrap-panel side-left" viewBox="0 0 740 344" role="img" aria-label="Side wrap panel, driver side">
  <rect width="740" height="344" fill="url(#rays-orange)"/>
  <rect x="200" y="112" width="540" height="128" fill="var(--band)"/>
  <rect x="200" y="108" width="540" height="5" fill="var(--grey)"/>
  <rect x="200" y="239" width="540" height="5" fill="var(--grey)"/>
  <polygon points="0,0 240,0 130,172 240,344 0,344" fill="var(--black)" role="img" aria-label="Dark panel with dot texture"/>
  <polygon points="240,0 266,0 156,172 266,344 240,344 130,172" fill="var(--white)"/>
  <circle cx="140" cy="172" r="100" fill="var(--grey-mark)" stroke="var(--white)" stroke-width="6"/>
  <polygon points="600,344 740,250 740,262 618,344" fill="#ff7a2a" opacity="0.7"/>

  <text class="services" x="281" y="94" textLength="439">INSULATION • FOUNDATION REPAIR • WATERPROOFING</text>
  <text class="brand-name" x="281" y="167" font-size="50" textLength="439" lengthAdjust="spacingAndGlyphs">BRICKNEST</text>
  <rect x="281" y="176" width="439" height="21" fill="var(--grey)"/>
  <text class="subtitle" x="300" y="192" textLength="401">SEAL AND SLAB</text>
  <text class="tagline" x="281" y="226" textLength="439">SEALED TIGHT, BUILT ON SOLID GROUND</text>
  <use href="#phone-icon" x="277" y="266" width="26" height="26"/>
  <text class="phone" x="309" y="289" textLength="211">(555) 214-7739</text>
  <rect x="277" y="298" width="243" height="20" rx="10" fill="var(--black)"/>
  <text class="web" x="398" y="312" text-anchor="middle">WWW.BRICKNEST-CREW.EXAMPLE</text>
</svg>

<!-- Passenger side -->
<svg class="wrap-panel side-right" viewBox="0 0 740 344" role="img" aria-label="Side wrap panel, passenger side">
  <rect width="740" height="344" fill="url(#rays-orange)"/>
  <rect x="0" y="112" width="540" height="128" fill="var(--band)"/>
  <rect x="0" y="108" width="540" height="5" fill="var(--grey)"/>
  <rect x="0" y="239" width="540" height="5" fill="var(--grey)"/>
  <g transform="translate(740 0) scale(-1 1)">
    <polygon points="0,0 240,0 130,172 240,344 0,344" fill="var(--black)" role="img" aria-label="Dark panel with dot texture"/>
    <polygon points="240,0 266,0 156,172 266,344 240,344 130,172" fill="var(--white)"/>
    <circle cx="140" cy="172" r="100" fill="var(--grey-mark)" stroke="var(--white)" stroke-width="6"/>
  </g>
  <polygon points="0,250 140,344 122,344 0,262" fill="#ff7a2a" opacity="0.7"/>

  <text class="services" x="32" y="94" textLength="435">INSULATION • FOUNDATION REPAIR • WATERPROOFING</text>
  <text class="brand-name" x="32" y="167" font-size="50" textLength="435" lengthAdjust="spacingAndGlyphs">BRICKNEST</text>
  <rect x="32" y="176" width="435" height="21" fill="var(--grey)"/>
  <text class="subtitle" x="51" y="192" textLength="397">SEAL AND SLAB</text>
  <text class="tagline" x="32" y="226" textLength="435">SEALED TIGHT, BUILT ON SOLID GROUND</text>
  <use href="#phone-icon" x="222" y="266" width="26" height="26"/>
  <text class="phone" x="254" y="289" textLength="212">(555) 214-7739</text>
  <rect x="222" y="298" width="245" height="20" rx="10" fill="var(--black)"/>
  <text class="web" x="344" y="312" text-anchor="middle">WWW.BRICKNEST-CREW.EXAMPLE</text>
</svg>

<!-- Rear door, orange -->
<svg class="wrap-panel door-orange" viewBox="0 0 450 420" role="img" aria-label="Rear roll-up door wrap, orange version">
  <rect width="450" height="420" fill="url(#rays-orange)"/>
  <polygon points="0,420 0,350 60,300 180,420" fill="#c92408" opacity="0.6"/>
  <rect x="0" y="142" width="450" height="140" fill="var(--band)"/>
  <rect x="0" y="138" width="450" height="6" fill="var(--grey)"/>
  <rect x="0" y="280" width="450" height="6" fill="var(--grey)"/>
  <circle cx="225" cy="84" r="68" fill="var(--grey-mark)" stroke="var(--white)" stroke-width="5"/>
  <text class="brand-name" x="36" y="206" font-size="44" textLength="378" lengthAdjust="spacingAndGlyphs">BRICKNEST</text>
  <rect x="36" y="214" width="378" height="20" fill="var(--grey)"/>
  <text class="subtitle" x="54" y="229" font-size="14" textLength="342">SEAL AND SLAB</text>
  <text class="tagline" x="36" y="262" textLength="378">SEALED TIGHT, BUILT ON SOLID GROUND</text>
  <text class="services" x="36" y="310" font-size="13" textLength="378">INSULATION • FOUNDATION REPAIR • WATERPROOFING</text>
  <use href="#phone-icon" x="118" y="320" width="24" height="24"/>
  <text class="phone" x="148" y="342" font-size="24" textLength="190">(555) 214-7739</text>
  <rect x="96" y="351" width="258" height="21" rx="10.5" fill="var(--black)"/>
  <text class="web" x="225" y="366" text-anchor="middle">WWW.BRICKNEST-CREW.EXAMPLE</text>
</svg>

<!-- Rear door, black -->
<svg class="wrap-panel door-black" viewBox="0 0 450 420" role="img" aria-label="Rear roll-up door wrap, black version">
  <rect width="450" height="420" fill="url(#rays-black)"/>
  <polygon points="0,420 0,350 60,300 180,420" fill="#2b2b2b"/>
  <rect x="0" y="142" width="450" height="140" fill="var(--band)"/>
  <rect x="0" y="138" width="450" height="6" fill="var(--grey)"/>
  <rect x="0" y="280" width="450" height="6" fill="var(--grey)"/>
  <circle cx="225" cy="84" r="68" fill="var(--grey-mark)" stroke="var(--white)" stroke-width="5"/>
  <text class="brand-name" x="36" y="206" font-size="44" textLength="378" lengthAdjust="spacingAndGlyphs">BRICKNEST</text>
  <rect x="36" y="214" width="378" height="20" fill="var(--grey)"/>
  <text class="subtitle" x="54" y="229" font-size="14" textLength="342">SEAL AND SLAB</text>
  <text class="tagline" x="36" y="262" textLength="378">SEALED TIGHT, BUILT ON SOLID GROUND</text>
  <text class="services" x="36" y="310" font-size="13" textLength="378" style="fill:var(--orange-light)">INSULATION • FOUNDATION REPAIR • WATERPROOFING</text>
  <use href="#phone-icon" x="118" y="320" width="24" height="24"/>
  <text class="phone" x="148" y="342" font-size="24" textLength="190">(555) 214-7739</text>
  <rect x="96" y="351" width="258" height="21" rx="10.5" fill="var(--orange)"/>
  <text class="web" x="225" y="366" text-anchor="middle">WWW.BRICKNEST-CREW.EXAMPLE</text>
</svg>

</body>
</html>
```